" Empresa em abertura de firma (status), voltada para o segmento de Headhunter / Jobhunter, Coaching e demais serviços administrativos/treinamento relacionados. "

```html
<!DOCTYPE html>
<html lang="pt-BR">
<head>
<meta charset="utf-8">
<title>RumoTalentos – Pasta institucional</title>
<link rel="stylesheet" href="https://fonts.googleapis.com/css2?family=Montserrat:wght@400;600;700&display=swap">
<style>
  :root {
    --bg: #ececef;
    --blue-deep: #2362c4;
    --blue-mid: #3f8fdc;
    --blue-light: #78c0ef;
    --blue-base: #2b59b8;
    --paper: #ffffff;
    --paper-shade: #f2f3f6;
    --ink: #2d4fa3;
    --ink-soft: #e9f3ff;
    --faint: rgba(255,255,255,0.22);
    --icon-phone: #9fd0ff;
    --icon-pin: #d04fb0;
    --icon-mail: #66b04a;
    --icon-social: #b8a86a;
  }
  * { margin: 0; padding: 0; box-sizing: border-box; }
  html, body { width: 1200px; height: 1200px; overflow: hidden; }
  body {
    background: var(--bg);
    font-family: "Montserrat", sans-serif;
    position: relative;
  }
  .folder-cover {
    position: absolute;
    left: 60px; top: 150px;
    width: 540px; height: 880px;
    border-radius: 14px 6px 6px 14px;
    background: linear-gradient(90deg, var(--blue-deep) 0%, var(--blue-mid) 55%, var(--blue-light) 100%);
    box-shadow: 0 10px 30px rgba(0,0,0,0.12);
    overflow: hidden;
  }
  .folder-cover::after {
    content: "";
    position: absolute; left: 0; right: 0; bottom: 0; height: 14px;
    background: var(--blue-base);
  }
  .cover-mark {
    position: absolute;
    left: 50%; top: 300px;
    transform: translateX(-50%);
    display: flex; flex-direction: column; align-items: center; gap: 26px;
  }
  .cover-mark-dot {
    width: 200px; height: 200px; border-radius: 50%;
    background: var(--faint);
  }
  .cover-mark-name {
    font-weight: 700; font-size: 46px; color: var(--faint);
    letter-spacing: 0.5px; white-space: nowrap;
  }
  .cover-contacts {
    position: absolute; left: 22px; right: 18px; bottom: 32px;
    display: flex; justify-content: space-between; align-items: center;
    gap: 10px;
    color: var(--ink-soft);
    font-size: 7.5px; line-height: 1.35;
  }
  .contact-item { display: flex; align-items: center; gap: 5px; flex: none; }
  .contact-item span { white-space: nowrap; }
  .contact-item svg { flex: none; }
  .folder-inside {
    position: absolute;
    left: 630px; top: 150px;
    width: 510px; height: 880px;
    background: var(--paper);
    border-radius: 4px;
    box-shadow: 0 10px 30px rgba(0,0,0,0.10);
    overflow: hidden;
  }
  .inside-pocket {
    position: absolute; left: 0; right: 0; bottom: 0; height: 430px;
    background: var(--paper);
    border-top: 1px solid #dfe2e8;
    box-shadow: 0 -6px 14px rgba(0,0,0,0.05);
  }
  .pocket-slit {
    position: absolute; left: 40px; top: -1px;
    width: 120px; height: 20px;
    border-bottom: 1px solid #dfe2e8;
    border-radius: 0 0 60px 60px;
  }
  .pocket-mark-faint {
    position: absolute; right: -40px; bottom: 40px;
    width: 260px; height: 260px; border-radius: 50%;
    background: var(--paper-shade);
  }
  .pocket-brand {
    position: absolute; left: 34px; bottom: 50px;
    display: flex; align-items: center; gap: 10px;
  }
  .brand-dot { width: 30px; height: 30px; border-radius: 50%; background: var(--ink); }
  .brand-name { font-weight: 700; font-size: 26px; color: var(--ink); white-space: nowrap; }
</style>
</head>
<body>
  <section class="folder-cover">
    <div class="cover-mark" aria-hidden="true">
      <div class="cover-mark-dot"></div>
      <div class="cover-mark-name">RumoTalentos</div>
    </div>
    <footer class="cover-contacts">
      <div class="contact-item">
        <svg width="10" height="10" viewBox="0 0 24 24"><path fill="var(--icon-phone)" d="M6.6 10.8a15 15 0 0 0 6.6 6.6l2.2-2.2a1 1 0 0 1 1-.25 11.4 11.4 0 0 0 3.6.57 1 1 0 0 1 1 1V20a1 1 0 0 1-1 1A17 17 0 0 1 3 4a1 1 0 0 1 1-1h3.5a1 1 0 0 1 1 1c0 1.25.2 2.45.57 3.57a1 1 0 0 1-.25 1z"/></svg>
        <span>(11) 4000-1234 | (11) 4000-5678</span>
      </div>
      <div class="contact-item">
        <svg width="12" height="9" viewBox="0 0 28 20"><rect x="1" y="1" width="26" height="18" rx="2" fill="var(--icon-mail)"/><path d="M2 2l12 9 12-9" stroke="#fff" stroke-width="2" fill="none"/></svg>
        <span>contato@rumotalentos.com</span>
      </div>
      <div class="contact-item">
        <svg width="9" height="13" viewBox="0 0 20 28"><path fill="var(--icon-pin)" d="M10 0a10 10 0 0 0-10 10c0 7.5 10 18 10 18s10-10.5 10-18A10 10 0 0 0 10 0zm0 14a4 4 0 1 1 0-8 4 4 0 0 1 0 8z"/></svg>
        <span>Rua das Acácias, 120,<br>Centro, São Paulo - SP</span>
      </div>
      <div class="contact-item">
        <svg width="10" height="10" viewBox="0 0 12 12"><circle cx="6" cy="6" r="6" fill="var(--icon-social)"/></svg>
        <span>@rumotalentos</span>
      </div>
    </footer>
  </section>

  <section class="folder-inside">
    <div class="inside-pocket">
      <div class="pocket-slit"></div>
      <div class="pocket-mark-faint" aria-hidden="true"></div>
      <div class="pocket-brand">
        <span class="brand-dot"></span>
        <span class="brand-name">RumoTalentos</span>
      </div>
    </div>
  </section>
</body>
</html>
```